I need a business card for myself, being a proprietor of a funeral parlor based in Manila. I'd like the card to have either of the following:
White Font on Black Background
or
Black Font on White Background
No logo is needed however I will appreciate any efforts to show a symbol of eternal happiness, aptly designed with above mentioned colors in mind.
Company name, address and contact on the lower right corner.
Logo or symbol anywhere.
Quillstone Funeral Services
+639174826351
darvik4521@pelmora.com
corner of Brisco Avenue and Velhurst Street
Makati City, Philippines
Thank you.
Update: Please include a small dove in your design. You are free to choose where you would like it on the card.

```html
<!DOCTYPE html>
<html lang="en">
<head>
<meta charset="utf-8">
<title>Quillstone Funeral Services — Business Card</title>
<link rel="stylesheet" href="https://fonts.googleapis.com/css2?family=Gelasio:wght@700&family=Open+Sans:ital,wght@0,400;1,300&display=swap">
<style>
  :root {
    --backdrop: #e9e7e4;
    --card: #3b3b3c;
    --card-edge: #333334;
    --name-ink: #161616;
    --rule: #1a1a1a;
    --contact-ink: #f4f4f4;
    --subtitle-ink: #1d1d1d;
    --emboss-tone: #454546;
    --emboss-tone-deep: #303031;
  }
  html, body {
    margin: 0;
    padding: 0;
    width: 1200px;
    height: 800px;
    overflow: hidden;
    background: var(--backdrop);
  }
  .canvas {
    position: relative;
    width: 1200px;
    height: 800px;
  }
  .business-card {
    position: absolute;
    left: 150px;
    top: 143px;
    width: 900px;
    height: 514px;
    background: var(--card);
    border: 1px solid var(--card-edge);
    box-sizing: border-box;
  }
  .laurel-branch {
    position: absolute;
    left: 70px;
    top: 40px;
    width: 150px;
    height: 290px;
    border-radius: 70px 70px 40px 40px;
    background: linear-gradient(160deg, var(--emboss-tone), var(--emboss-tone-deep));
  }
  .dove {
    position: absolute;
    left: 240px;
    top: 90px;
    width: 70px;
    height: 55px;
    border-radius: 50%;
    background: linear-gradient(160deg, var(--emboss-tone), var(--emboss-tone-deep));
  }
  .company-name {
    position: absolute;
    right: 60px;
    top: 110px;
    margin: 0;
    font-family: "Gelasio", Georgia, serif;
    font-weight: 700;
    font-size: 62px;
    letter-spacing: 1px;
    color: var(--name-ink);
    line-height: 1;
  }
  .name-rule {
    position: absolute;
    left: 470px;
    right: 60px;
    top: 196px;
    height: 3px;
    background: var(--rule);
  }
  .company-trade {
    position: absolute;
    right: 60px;
    top: 206px;
    margin: 0;
    font-family: "Open Sans", Arial, sans-serif;
    font-style: italic;
    font-weight: 300;
    font-size: 30px;
    color: var(--subtitle-ink);
    line-height: 1;
  }
  .contact-details {
    position: absolute;
    right: 60px;
    top: 270px;
    margin: 0;
    font-family: "Open Sans", Arial, sans-serif;
    font-style: normal;
    font-size: 24px;
    line-height: 34px;
    color: var(--contact-ink);
    text-align: right;
  }
  .contact-details span { display: block; }
</style>
</head>
<body>
  <main class="canvas">
    <section class="business-card" aria-label="Quillstone Funeral Services business card">
      <div class="laurel-branch" role="img" aria-label="Embossed laurel branch symbolising eternal happiness"></div>
      <div class="dove" role="img" aria-label="Small embossed dove in flight"></div>

      <h1 class="company-name">Quillstone</h1>
      <div class="name-rule"></div>
      <p class="company-trade">funeral services</p>

      <address class="contact-details">
        <span class="contact-phone">+639174826351</span>
        <span class="contact-email">darvik4521@pelmora.com</span>
        <span class="contact-street">corner of Brisco Avenue and Velhurst Street</span>
        <span class="contact-city">Makati City, Philippines</span>
      </address>
    </section>
  </main>
</body>
</html>
```